Varek services highend custom homes

We build high end custom homes and timber frames we specialize in rustic hand made designs along with iron and concrete accents to add a modern touch 90% of my homes are buit on lake front properries attached is my logo and slogan as of now and my previous one

Target Market(s)

High end custom homes

Industry/Entity Type

Custom residential construction

Contact Information for Business Card

Been in buissness 8+ years inssured and reliable

Colors
A7469A
B969AE
D3A5CF
EDDBEB
F8F0F9

Requirements
Must have
• Must have slogan and phone number
Should not have
• A combination of rustic yet modern accents

```html
<!DOCTYPE html>
<html lang="en">
<head>
<meta charset="utf-8">
<title>Varek Services — Business Card</title>
<link href="https://fonts.googleapis.com/css2?family=Montserrat:wght@400;500;700;800&display=swap" rel="stylesheet">
<style>
  :root {
    --backdrop: #3b3b3b;
    --card: #141414;
    --card-edge: #4d5a48;
    --sage: #5f6e58;
    --ink-light: #f2f2f2;
    --gloss: #4a4a4a;
    --divider: #3a3a3a;
  }
  * { margin: 0; padding: 0; box-sizing: border-box; }
  html, body {
    width: 1200px; height: 801px; overflow: hidden;
    background: var(--backdrop);
    font-family: "Montserrat", Arial, sans-serif;
  }
  .stage {
    position: relative; width: 1200px; height: 801px;
    display: flex; align-items: center; justify-content: center; gap: 50px;
  }
  .card {
    position: relative; width: 525px; height: 300px;
    background: var(--card);
    border-bottom: 2px solid var(--card-edge);
    box-shadow: 0 10px 28px rgba(0,0,0,.45);
  }
  /* Contact side */
  .card--contact { display: flex; align-items: center; }
  .brand-block {
    width: 265px; height: 100%; padding: 0 16px;
    display: flex; flex-direction: column; align-items: center; justify-content: center;
    gap: 10px;
  }
  .brand-mark { display: flex; align-items: center; gap: 8px; white-space: nowrap; }
  .brand-square { width: 16px; height: 16px; background: var(--sage); flex: none; }
  .brand-name {
    color: var(--sage); font-weight: 800; font-size: 19px;
    letter-spacing: .4px; text-transform: uppercase;
  }
  .slogan {
    color: var(--sage); font-weight: 500; font-size: 10px;
    letter-spacing: 1.4px; text-transform: uppercase; white-space: nowrap;
    display: flex; align-items: center; gap: 6px;
  }
  .slogan::before, .slogan::after {
    content: ""; width: 5px; height: 5px; border: 1px solid var(--sage); border-radius: 50%;
  }
  .divider { width: 1px; height: 170px; background: var(--divider); flex: none; }
  .details {
    padding-left: 26px; color: var(--ink-light); font-size: 13px; line-height: 1.4;
    white-space: nowrap;
  }
  .person-name {
    color: var(--sage); font-weight: 700; font-size: 17px; letter-spacing: 1px;
    text-transform: uppercase;
  }
  .person-role { margin-bottom: 14px; }
  .address { margin-bottom: 14px; }
  .contact-list { list-style: none; }
  .contact-list li { display: flex; align-items: center; gap: 8px; }
  .contact-list svg { width: 11px; height: 11px; flex: none; }
  .icon-fill { fill: var(--sage); }
  .icon-stroke { fill: none; stroke: var(--sage); stroke-width: 2.5; }
  /* Brand side */
  .card--brand {
    display: flex; flex-direction: column; align-items: center; justify-content: center; gap: 12px;
  }
  .card--brand .brand-square { width: 30px; height: 30px; background: var(--gloss); }
  .card--brand .brand-name { color: var(--gloss); font-size: 38px; }
  .card--brand .slogan { color: var(--gloss); font-size: 13px; letter-spacing: 2px; }
  .card--brand .slogan::before, .card--brand .slogan::after { border-color: var(--gloss); }
</style>
</head>
<body>
<main class="stage">
  <section class="card card--contact">
    <div class="brand-block">
      <div class="brand-mark">
        <span class="brand-square"></span>
        <span class="brand-name">Varek Services</span>
      </div>
      <p class="slogan">From lodges to estates</p>
    </div>
    <div class="divider"></div>
    <div class="details">
      <p class="person-name">Marcus Dalby</p>
      <p class="person-role">President</p>
      <p class="address">1840 Harbor Crest Way<br>Cedar Cove CA 92410</p>
      <ul class="contact-list">
        <li><svg viewBox="0 0 24 24"><path class="icon-fill" d="M6.6 10.8a15 15 0 0 0 6.6 6.6l2.2-2.2a1 1 0 0 1 1-.25 11.4 11.4 0 0 0 3.6.57 1 1 0 0 1 1 1V20a1 1 0 0 1-1 1A17 17 0 0 1 3 4a1 1 0 0 1 1-1h3.5a1 1 0 0 1 1 1c0 1.25.2 2.45.57 3.57a1 1 0 0 1-.25 1z"/></svg>555-240-6188</li>
        <li><svg viewBox="0 0 24 24"><rect class="icon-stroke" x="2" y="5" width="20" height="14"/><path class="icon-stroke" d="M2 5l10 8 10-8"/></svg>marcus@varekservices.com</li>
        <li><svg viewBox="0 0 24 24"><circle class="icon-fill" cx="12" cy="12" r="10"/></svg>www.varekservices.com</li>
      </ul>
    </div>
  </section>

  <section class="card card--brand">
    <div class="brand-mark">
      <span class="brand-square"></span>
      <span class="brand-name">Varek Services</span>
    </div>
    <p class="slogan">From lodges to estates</p>
  </section>
</main>
</body>
</html>
```